New website for tarnova.se using wordpress

- Tarnova is a consultant broker based in Sweden
- Current web page: tarnova.se
- We want a new web page and we are aiming for simple and "clean"
- Two target groups:
1. Consultants/Consultant firms looking for assignments
2. Clients looking for consultants
- Colors + Logo attached

Requirements
Must have
• The new site should have separate pages the different sections. We have to be able to link to each page separately. NOT like the current web page where all the content is on one page.

```html
<!DOCTYPE html>
<html lang="sv">
<head>
<meta charset="utf-8">
<title>Tarnova – Konsultmäklare</title>
<link href="https://fonts.googleapis.com/css2?family=Poppins:wght@400;500;600;700;800&display=swap" rel="stylesheet">
<style>
:root{
  --purple:#65339a;
  --lavender:#d9c8ef;
  --lavender-soft:#e8e0f2;
  --ink:#2b2b2b;
  --dark-btn:#333333;
  --black:#000000;
  --white:#ffffff;
}
*{margin:0;padding:0;box-sizing:border-box}
html,body{width:1200px;height:3117px;overflow:hidden}
body{font-family:"Poppins",sans-serif;color:var(--ink);position:relative;background:var(--white)}
.abs{position:absolute}

/* header */
.site-header{left:0;top:0;width:1200px;height:68px;background:var(--purple);z-index:5}
.logo-tab{left:79px;top:0;width:263px;height:94px;background:var(--purple);border-radius:0 0 26px 26px;z-index:6;
  display:flex;align-items:center;justify-content:center;color:var(--white);font-weight:700;font-size:50px;letter-spacing:1px;padding-bottom:10px}
.main-nav{top:23px;z-index:6;display:flex;left:455px;gap:0}
.main-nav a{position:absolute;top:0;color:var(--white);font-weight:700;font-size:16px;text-decoration:none;white-space:nowrap;letter-spacing:.3px}

/* hero */
.hero{left:0;top:68px;width:1200px;height:716px;
  background:linear-gradient(180deg,#4d6f8c 0%,#7d7a70 25%,#a0683e 50%,#8a5a34 68%,#3f4a48 82%,#27353b 100%)}
.hero-title{left:0;top:290px;width:1200px;text-align:center;color:var(--white);font-weight:800;font-size:68px;line-height:76px;letter-spacing:1px}
.hero-btn{top:479px;width:218px;height:56px;border:2px solid var(--white);border-radius:30px;background:var(--purple);
  color:var(--white);font-weight:700;font-size:17px;display:flex;align-items:center;justify-content:center}

/* shared */
.photo-shadow{background:var(--lavender);border-radius:46px 10px 46px 46px}
.photo{border-radius:40px 40px 40px 10px}
.section-title{font-weight:800;font-size:46px;line-height:52px;color:var(--purple)}
.pill-btn{border-radius:30px;color:var(--white);font-weight:700;font-size:19px;display:flex;align-items:center;justify-content:center}

/* about */
.about{left:0;top:784px;width:1200px;height:616px;background:linear-gradient(180deg,var(--lavender-soft) 0%,#ffffff 80%)}
.about-text{left:616px;top:948px;width:520px;font-size:15.5px;line-height:32.4px;color:#333}

/* assignments */
.assignments{left:0;top:1400px;width:1200px;height:694px;background:var(--purple)}
.assign-box{left:75px;top:1461px;width:722px;height:571px;border:2px solid var(--white);border-radius:38px}
.assign-title{left:104px;top:1506px;color:var(--white)}
.assign-list{left:104px;top:1633px;width:480px;list-style:none;color:var(--white);font-size:15.5px;line-height:27px}
.assign-list li{position:relative;padding-left:33px;margin-bottom:11px}
.assign-list svg{position:absolute;left:0;top:6px}

/* why */
.why-list{left:641px;top:2322px;list-style:none;font-size:18px;color:#333}
.why-list li{position:relative;padding-left:35px;height:40.7px;line-height:30px}
.why-list svg{position:absolute;left:0;top:8px}

/* footer */
.site-footer{left:0;top:2680px;width:1200px;height:437px;background:var(--black);color:var(--white)}
.footer-heading{font-weight:700;font-size:27px;color:var(--lavender)}
.footer-line{font-size:16.5px;color:var(--white);white-space:nowrap}
.footer-icon{position:absolute;left:0;top:3px}
.social{left:433px;top:2797px;display:flex;gap:12px}
.social span{width:26px;height:26px;border-radius:50%;background:var(--white);display:block}
.divider{left:0;top:3036px;width:1200px;height:1px;background:#222}
.copyright{left:0;top:3062px;width:1200px;text-align:center;font-size:15.5px}
</style>
</head>
<body>

<header class="abs site-header"></header>
<div class="abs logo-tab">TARNOVA</div>
<nav class="abs main-nav" aria-label="Huvudmeny">
  <a style="left:0">CONSULTANT</a>
  <a style="left:160px">CLIENT</a>
  <a style="left:262px">ASSIGNMENTS</a>
  <a style="left:431px">ABOUT US</a>
  <a style="left:560px">CONTACT US</a>
</nav>

<section class="abs hero" role="img" aria-label="Flygfoto över Stockholms gamla stad vid vattnet"></section>
<h1 class="abs hero-title">VI HJÄLPER DITT FÖRETAG<br>ATT VÄXA.</h1>
<a class="abs hero-btn" style="left:369px">CONSULTANT</a>
<a class="abs hero-btn" style="left:617px">CLIENTS</a>

<section class="abs about"></section>
<div class="abs photo-shadow" style="left:60px;top:880px;width:527px;height:436px"></div>
<div class="abs photo" style="left:75px;top:866px;width:512px;height:438px;background:linear-gradient(135deg,#c9d3dc,#6d6f78 60%,#3e414a)" role="img" aria-label="Affärsmöte med konsulter kring en bärbar dator"></div>
<h2 class="abs section-title" style="left:616px;top:862px">ABOUT US</h2>
<p class="abs about-text">Sed ut perspiciatis unde omnis iste natus error sit voluptatem accusantium doloremque laudantium, totam rem aperiam, eaque ipsa quae ab illo inventore veritatis et quasi architecto beatae vitae dicta sunt explicabo. Nemo enim ipsam voluptatem consequuntur magni dolores eos qui ratione voluptatem enim ipsam voluptatem quia voluptas sit aspernatur aut odit aut fugit, sed quia consequuntur magni dolores eos qui ratione voluptatem sequi nesciunt. Neque porro quisquam est, qui dolorem ipsum quia dolor sit amet.</p>
<a class="abs pill-btn" style="left:616px;top:1243px;width:224px;height:57px;background:var(--dark-btn)">READ MORE</a>

<section class="abs assignments"></section>
<div class="abs assign-box"></div>
<h2 class="abs section-title assign-title">MOST RECENT<br>ASSIGNMENTS</h2>
<ul class="abs assign-list">
  <li><svg width="14" height="14" viewBox="0 0 14 14"><circle cx="7" cy="7" r="7" fill="#fff"/><path d="M3.8 7.2l2.2 2.1 4.2-4.3" stroke="#65339a" stroke-width="1.8" fill="none"/></svg>Sed ut perspiciatis unde omnis iste natus error sit voluptatemaccusantium doloremque.</li>
  <li><svg width="14" height="14" viewBox="0 0 14 14"><circle cx="7" cy="7" r="7" fill="#fff"/><path d="M3.8 7.2l2.2 2.1 4.2-4.3" stroke="#65339a" stroke-width="1.8" fill="none"/></svg>Audantium, totam rem aperiam, eaque ipsa quae.</li>
  <li><svg width="14" height="14" viewBox="0 0 14 14"><circle cx="7" cy="7" r="7" fill="#fff"/><path d="M3.8 7.2l2.2 2.1 4.2-4.3" stroke="#65339a" stroke-width="1.8" fill="none"/></svg>Ab illo inventore veritatis et quasi architecto beatae vitae dicta sunt explicabo.</li>
  <li><svg width="14" height="14" viewBox="0 0 14 14"><circle cx="7" cy="7" r="7" fill="#fff"/><path d="M3.8 7.2l2.2 2.1 4.2-4.3" stroke="#65339a" stroke-width="1.8" fill="none"/></svg>Consequuntur magni dolores eos qui ratione voluptatem.</li>
  <li><svg width="14" height="14" viewBox="0 0 14 14"><circle cx="7" cy="7" r="7" fill="#fff"/><path d="M3.8 7.2l2.2 2.1 4.2-4.3" stroke="#65339a" stroke-width="1.8" fill="none"/></svg>Voluptas sit aspernatur aut odit aut fugit, sed quia conse quuntur magni dolores eos.</li>
</ul>
<a class="abs pill-btn" style="left:104px;top:1923px;width:224px;height:57px;background:var(--black)">ABOUT US</a>
<div class="abs photo-shadow" style="left:640px;top:1541px;width:500px;height:435px;border-radius:46px 46px 46px 46px"></div>
<div class="abs photo" style="left:615px;top:1527px;width:511px;height:435px;background:linear-gradient(135deg,#e9ecef,#b9c2cc 55%,#3d4a66)" role="img" aria-label="Konsult vid skrivbord med dokument och miniräknare"></div>

<div class="abs photo-shadow" style="left:75px;top:2172px;width:526px;height:438px"></div>
<div class="abs photo" style="left:90px;top:2158px;width:511px;height:437px;background:linear-gradient(135deg,#d5dbe0,#8a9bb3 50%,#2f3c55)" role="img" aria-label="Två kollegor tittar på en surfplatta"></div>
<h2 class="abs section-title" style="left:641px;top:2249px">WHY TARNOVA</h2>
<ul class="abs why-list">
  <li><svg width="17" height="13" viewBox="0 0 17 13"><path d="M1.5 6.5l4.5 4.5 9.5-9.5" stroke="#65339a" stroke-width="3" fill="none"/></svg>Transparenta kring pris</li>
  <li><svg width="17" height="13" viewBox="0 0 17 13"><path d="M1.5 6.5l4.5 4.5 9.5-9.5" stroke="#65339a" stroke-width="3" fill="none"/></svg>Kvalitativt nätverk och samtidigt oberoende</li>
  <li><svg width="17" height="13" viewBox="0 0 17 13"><path d="M1.5 6.5l4.5 4.5 9.5-9.5" stroke="#65339a" stroke-width="3" fill="none"/></svg>Feta ramavtal med otroligt nöjda kunder</li>
  <li><svg width="17" height="13" viewBox="0 0 17 13"><path d="M1.5 6.5l4.5 4.5 9.5-9.5" stroke="#65339a" stroke-width="3" fill="none"/></svg>Snabba och personliga</li>
  <li><svg width="17" height="13" viewBox="0 0 17 13"><path d="M1.5 6.5l4.5 4.5 9.5-9.5" stroke="#65339a" stroke-width="3" fill="none"/></svg>Anser återkoppling och dialog är viktigt</li>
</ul>

<footer class="abs site-footer"></footer>
<h3 class="abs footer-heading" style="left:75px;top:2740px">Kontakt</h3>
<div class="abs footer-line" style="left:75px;top:2794px;padding-left:34px;line-height:29px">
  <svg class="footer-icon" style="top:7px" width="18" height="14" viewBox="0 0 18 14"><path d="M1 2l5-1.5 6 2 5-1.5v11l-5 1.5-6-2-5 1.5z" fill="#fff"/></svg>
  Hornsgatan 42 118<br>20 Stockholm</div>
<div class="abs footer-line" style="left:75px;top:2862px;padding-left:34px">
  <svg class="footer-icon" width="14" height="16" viewBox="0 0 14 16"><path d="M3 1l3 3-1.5 2c1 2 2.5 3.5 4.5 4.5l2-1.5 3 3-2 3C6 14 0 8 1 3z" fill="#fff"/></svg>
  +46 (0) 8-555 123 40</div>
<div class="abs footer-line" style="left:75px;top:2901px;padding-left:34px">
  <svg class="footer-icon" style="top:5px" width="16" height="12" viewBox="0 0 16 12"><rect width="16" height="12" rx="1" fill="#fff"/><path d="M0 1l8 5 8-5" stroke="#000" stroke-width="1.4" fill="none"/></svg>
  info@tarnova.se</div>

<h3 class="abs footer-heading" style="left:433px;top:2740px">Följ Oss</h3>
<div class="abs social" aria-label="Sociala medier"><span></span><span></span><span></span><span></span></div>

<h3 class="abs footer-heading" style="left:764px;top:2740px">Meny</h3>
<div class="abs footer-line" style="left:764px;top:2794px">Consultant</div>
<div class="abs footer-line" style="left:764px;top:2838px">Client</div>
<div class="abs footer-line" style="left:764px;top:2882px">Assignments</div>
<div class="abs footer-line" style="left:764px;top:2925px">About Us</div>
<div class="abs footer-line" style="left:764px;top:2969px">Contact Us</div>

<div class="abs divider"></div>
<p class="abs copyright">© Tarnova.se 2022 - Tarnova ingår i Veltra AB</p>

</body>
</html>
```